Design a FUN and AWESOME Aviation Website Design for Kestrel Haven

We need a homepage website design for "Kestrel Haven".
We're looking to complete this quickly, so if we get a great design in the next few days, we will end the contest early and select a winner!
What the Site Will Do
This site will be for pilots to rent aircraft (mostly prop planes, but jets and helicopters will be possible as well) as well as the general public to charter flights. Also the ability to buy and sell aircraft. There will also be information to lookup airports by their Our crew or IATA codes. And information for learning to fly including finding flight schools plus flight clubs.
What We Like
We love the mockup designs for Morrow Glide (see 8 MorrowGlide attachments)
The elements we especially like in their designs are...
- the departure board style split-flap letters and numbers plus the split-flaps with icons
- the red, white and blue edging that represents airmail
- the gradient light effects in the colors
- the yellow colors used
- the black split-flap departure board with the letters flying off
- we also like the idea of the large photo being used
We also like the idea of airport signage. Veldmoor airport in Amsterdam has good signage which can be seen here: [login to view URL]
Using Avionics elements might be cool too: [login to view URL]
I have included a couple of other website designs that we thought were interesting.
And did I say we really like the MorrowGlide designs? :)
Navigation
Home, Aircraft, Airports, Pilots, Passengers, Events, Members (Home would be optional since the logo would ultimately work for that)
The navigation will also need megamenu drop downs designed for Aircraft as well as drop down menus for Airports, Pilots, and Passengers.
Logo
We do not have a logo yet and it is currently being designed in another contest. You can use text for now.
UPDATE: WE HAVE A LOGO NOW - IT IS ATTACHED
Colors
We like blue (like the blue attachments)
We like orange (like the orange gradient in the orange attachment and used here: [login to view URL])
We like yellow (like the gradients in the attached MorrowGlide images)
We like gradient blacks (like the split-flap departure boards attached)
But seriously, we're open to whatever colors you come up with. If you choose a color that we don't like, we'll let you know.
The Best Looking Aviation Sites
[login to view URL]
[login to view URL]
[login to view URL]
[login to view URL]
The final design should be provided in an Adobe Photoshop .PSD format file and should have well named layers. The design should be large enough to fill the width of an HD monitor (1920px) without having large margins.

```html
<!DOCTYPE html>
<html lang="en">
<head>
<meta charset="utf-8">
<title>Kestrel Haven</title>
<link rel="stylesheet" href="https://fonts.googleapis.com/css2?family=Open+Sans:wght@400;600;700&family=Oswald:wght@500&display=swap">
<style>
:root{
  --ink:#231f20;
  --bar:#3b3738;
  --flap:#151314;
  --yellow:#f9c22e;
  --yellow-light:#fbd94c;
  --orange:#f6a320;
  --white:#ffffff;
  --red:#e2262b;
  --tag-orange:#f5a623;
}
*{box-sizing:border-box;margin:0;padding:0}
html,body{width:1200px;height:883px;overflow:hidden;background:var(--white)}
body{position:relative;font-family:"Open Sans",Arial,sans-serif;color:var(--white)}
.abs{position:absolute}

/* top bar */
.topbar{left:0;top:0;width:1200px;height:51px;background:var(--ink)}
.search{left:891px;top:13px;width:156px;height:24px;background:var(--white);display:flex}
.search span{flex:1;font-size:9px;color:#999;padding:6px 8px}
.search i{width:24px;background:var(--yellow);display:flex;align-items:center;justify-content:center}
.social{display:flex;gap:10px}
.social b{width:11px;height:11px;border-radius:50%;background:var(--white);display:block}
.social-top{left:1066px;top:20px}

/* sidebar */
.sidebar{left:0;top:0;width:181px;height:509px;background:linear-gradient(180deg,#2b2728,var(--ink))}
.brand{left:31px;top:33px;width:120px;height:24px;border:1.5px solid var(--yellow);font-size:13.5px;font-weight:600;text-align:center;line-height:21px;text-transform:uppercase}
.nav{left:0;top:91px;width:181px;list-style:none}
.nav li{height:33px;line-height:33px;text-align:center;font-size:13.5px;font-weight:600;text-transform:uppercase}
.nav li.active{background:var(--yellow)}

/* hero */
.hero{left:181px;top:51px;width:1019px;height:416px;
  background:
    radial-gradient(ellipse 520px 260px at 100% 20%,rgba(226,221,212,.95) 0%,rgba(214,208,198,.7) 45%,rgba(200,195,188,0) 100%),
    radial-gradient(ellipse 420px 120px at 55% 78%,rgba(236,238,240,.55) 0%,rgba(236,238,240,0) 100%),
    linear-gradient(180deg,#c7d0d8 0%,#aab4bd 18%,#7d858c 30%,#5b636b 42%,#3f4b57 58%,#2f3d4a 72%,#4a4f55 86%,#5a5b5d 100%);}
.caption{background:var(--yellow);font-size:22px;font-weight:600;text-transform:uppercase;line-height:30px;padding:0 8px;text-align:right}
.caption-1{right:32px;top:231px}
.caption-2{right:32px;top:261px}
.caption-arrow{left:1168px;top:267px}
.dots{left:577px;top:435px;display:flex;gap:6px}
.dots b{width:11px;height:11px;border-radius:50%;border:2px solid var(--white);display:block}
.dots b.on{border-color:var(--yellow)}

/* booking bar */
.booking{left:181px;top:467px;height:42px;display:flex;background:var(--bar)}
.booking .lead{width:64px;background:var(--yellow)}
.booking .label{padding:0 14px;font-size:12.5px;font-weight:600;line-height:42px;text-transform:uppercase;border-left:1px solid #4a4546}
.flap{width:26px;background:var(--flap);font-family:"Oswald",sans-serif;font-size:21px;line-height:42px;text-align:center;border-left:1px solid #2a2627;position:relative}
.flap-num{width:41px}
.flap::after{content:"";position:absolute;left:0;right:0;top:21px;height:1px;background:#3a3637}
.icon-tile{width:42px;background:var(--flap);display:flex;align-items:center;justify-content:center;border-left:1px solid #2a2627}
.go{width:54px;background:var(--yellow);font-size:13px;font-weight:600;line-height:42px;text-align:center;margin-left:3px}
.more-btn{width:29px;background:var(--yellow);margin-left:3px;display:flex;align-items:center;justify-content:center}

/* carousel */
.arrow-btn{width:39px;height:39px;display:flex;align-items:center;justify-content:center}
.arrow-prev{left:41px;top:569px;border:1.5px solid var(--ink)}
.arrow-next{left:1120px;top:569px;border:1.5px solid var(--yellow)}
.card{top:539px;width:173px;height:101px;border:4px solid #f1f1f1;box-shadow:0 6px 8px rgba(0,0,0,.25)}
.card .photo{width:100%;height:100%}
.tag{position:absolute;left:-2px;top:-3px;font-size:7px;font-weight:700;text-transform:uppercase;padding:1px 5px}
.tag-red{background:var(--red)}
.tag-orange{background:var(--tag-orange)}

/* feature band */
.band{left:0;top:669px;width:1200px;height:171px;background:linear-gradient(180deg,var(--yellow-light) 0%,#f9c63a 45%,var(--orange) 100%)}
.field{left:184px;width:173px;background:var(--white);font-size:9px;color:#8c8c8c;padding:5px 9px}
.field-name{top:695px;height:22px}
.field-email{top:724px;height:23px}
.field-msg{top:753px;height:36px}
.btn-outline{border:1px solid var(--white);font-size:8.5px;text-transform:uppercase;text-align:center;line-height:13px}
.btn-contact{left:184px;top:799px;width:57px;height:15px}
.divider{top:693px;width:1px;height:107px;background:rgba(255,255,255,.7)}
.video{left:516px;top:695px;width:172px;height:101px;border:3px solid var(--white);box-shadow:0 6px 8px rgba(0,0,0,.25);
  background:radial-gradient(ellipse 60px 50px at 35% 60%,rgba(40,48,62,.55),rgba(40,48,62,0)),linear-gradient(180deg,#eef1f4 0%,#dfe5ea 55%,#b9bfc4 100%)}
.play{left:580px;top:728px}
.story{left:843px;top:692px;width:188px;font-size:9px;line-height:13.4px}
.btn-more{left:843px;top:789px;width:43px;height:15px}

/* footer */
.footer{left:0;top:840px;width:1200px;height:43px;background:var(--ink)}
.footer-nav{left:31px;top:855px;display:flex;list-style:none;font-size:11.5px;text-transform:uppercase}
.footer-nav li+li::before{content:"|";margin:0 10px}
.signup{left:860px;top:849px;width:187px;height:24px;display:flex}
.signup span{flex:1;background:var(--white);color:#888;font-size:9px;padding:6px 9px}
.signup b{width:47px;background:var(--yellow);font-size:11px;font-weight:600;text-align:center;line-height:24px}
.social-foot{left:1066px;top:856px}
</style>
</head>
<body>

<div class="abs topbar"></div>
<div class="abs search"><span>Search...</span><i><svg width="10" height="10" viewBox="0 0 10 10"><circle cx="4" cy="4" r="3" fill="none" stroke="#fff" stroke-width="1.5"/><line x1="6.3" y1="6.3" x2="9" y2="9" stroke="#fff" stroke-width="1.5"/></svg></i></div>
<div class="abs social social-top" aria-label="Social links"><b></b><b></b><b></b><b></b><b></b></div>

<aside class="abs sidebar"></aside>
<div class="abs brand">Kestrel Haven</div>
<ul class="abs nav">
  <li class="active">Home</li>
  <li>Aircraft</li>
  <li>Airports</li>
  <li>Pilots</li>
  <li>Passengers</li>
  <li>Events</li>
  <li>Members</li>
  <li>Contact</li>
</ul>

<div class="abs hero" role="img" aria-label="Aerial view of a city skyline and river seen past an airliner wing"></div>
<div class="abs caption caption-1">Dummy text for this slide</div>
<div class="abs caption caption-2">Goes here</div>
<svg class="abs caption-arrow" width="6" height="10" viewBox="0 0 6 10"><path d="M0 0 L6 5 L0 10Z" fill="#fff"/></svg>
<div class="abs dots"><b></b><b class="on"></b><b></b></div>

<div class="abs booking">
  <div class="lead"></div>
  <div class="label">Escape from</div>
  <div class="flap">S</div><div class="flap">T</div><div class="flap">D</div>
  <div class="label">On</div>
  <div class="flap flap-num">26</div><div class="flap flap-num">27</div><div class="flap flap-num">28</div>
  <div class="label">Show me</div>
  <div class="icon-tile"><svg width="24" height="24" viewBox="0 0 24 24"><circle cx="12" cy="12" r="5" fill="#fff"/><g stroke="#fff" stroke-width="2"><line x1="12" y1="1" x2="12" y2="4"/><line x1="12" y1="20" x2="12" y2="23"/><line x1="1" y1="12" x2="4" y2="12"/><line x1="20" y1="12" x2="23" y2="12"/><line x1="4" y1="4" x2="6" y2="6"/><line x1="18" y1="18" x2="20" y2="20"/><line x1="4" y1="20" x2="6" y2="18"/><line x1="18" y1="6" x2="20" y2="4"/></g></svg></div>
  <div class="label">With</div>
  <div class="icon-tile"><svg width="24" height="24" viewBox="0 0 24 24" aria-label="Dining"><g fill="#fff"><path d="M3 21 L15 9 L16.5 10.5 L4.5 22.5Z"/><path d="M15 9 C14 5 17 2 21 2 C22 6 19 10 16.5 10.5Z"/></g><g stroke="#fff" stroke-width="1.6" fill="none" stroke-linecap="round"><line x1="20" y1="21" x2="9" y2="10"/><path d="M9 10 L4 5"/><path d="M4 5 L7.5 1.5 M5.7 6.7 L9.2 3.2 M7.4 8.4 L10.9 4.9"/></g></svg></div>
  <div class="icon-tile"><svg width="22" height="22" viewBox="0 0 22 22"><path d="M3 3 H19 L11 12Z" fill="#fff"/><line x1="11" y1="12" x2="11" y2="19" stroke="#fff" stroke-width="2"/><line x1="7" y1="20" x2="15" y2="20" stroke="#fff" stroke-width="2"/><circle cx="17" cy="3" r="2" fill="#fff"/></svg></div>
  <div class="go">GO</div>
  <div class="more-btn"><svg width="11" height="7" viewBox="0 0 11 7"><path d="M1 1 L5.5 5.5 L10 1" fill="none" stroke="#fff" stroke-width="1.6"/></svg></div>
</div>

<div class="abs arrow-btn arrow-prev"><svg width="18" height="18" viewBox="0 0 18 18"><path d="M16 1 L2 9 L16 17 L11 9Z" fill="#231f20"/></svg></div>
<div class="abs arrow-btn arrow-next"><svg width="18" height="18" viewBox="0 0 18 18"><path d="M2 1 L16 9 L2 17 L7 9Z" fill="#f9c22e"/></svg></div>

<div class="abs card" style="left:120px"><div class="photo" role="img" aria-label="Red racing prop plane on a runway" style="background:radial-gradient(ellipse 60px 18px at 45% 45%,rgba(200,30,35,.85),rgba(200,30,35,0)),linear-gradient(180deg,#e4e8f0 0%,#d6d8e6 40%,#c9a898 70%,#e3b9a3 100%)"></div><span class="tag tag-red">New</span></div>
<div class="abs card" style="left:316px"><div class="photo" role="img" aria-label="Red biplane flying over water" style="background:radial-gradient(ellipse 62px 20px at 45% 40%,rgba(196,38,30,.85),rgba(196,38,30,0)),linear-gradient(180deg,#5d92c9 0%,#9fc3e3 50%,#d7dde2 75%,#8ea3b4 100%)"></div><span class="tag tag-red">Sell</span></div>
<div class="abs card" style="left:512px"><div class="photo" role="img" aria-label="Cartoon prop plane flying over hills" style="background:radial-gradient(ellipse 55px 20px at 45% 40%,rgba(235,150,60,.8),rgba(235,150,60,0)),linear-gradient(180deg,#8fc6ec 0%,#c9e4f4 55%,#7fa9c3 80%,#9bc0d4 100%)"></div><span class="tag tag-orange">Prop</span></div>
<div class="abs card" style="left:708px"><div class="photo" role="img" aria-label="Fighter jet in flight" style="background:radial-gradient(ellipse 60px 16px at 50% 45%,rgba(240,242,248,.95),rgba(60,80,170,.5) 60%,rgba(60,80,170,0)),linear-gradient(180deg,#7fb2e0,#c4dcf0)"></div><span class="tag tag-orange">Jet</span></div>
<div class="abs card" style="left:904px"><div class="photo" role="img" aria-label="Red and white helicopter in flight" style="background:radial-gradient(ellipse 50px 18px at 50% 45%,rgba(205,40,35,.85),rgba(205,40,35,0)),linear-gradient(180deg,#d3e5f3,#a6c6e2)"></div><span class="tag tag-orange">Helicopter</span></div>

<section class="abs band"></section>
<div class="abs field field-name">Name</div>
<div class="abs field field-email">Email</div>
<div class="abs field field-msg">Message</div>
<div class="abs btn-outline btn-contact">Contact</div>
<div class="abs divider" style="left:437px"></div>
<div class="abs divider" style="left:764px"></div>
<div class="abs video" role="img" aria-label="Video still of a pilot with a tablet beside a private jet"></div>
<svg class="abs play" width="36" height="36" viewBox="0 0 36 36"><circle cx="18" cy="18" r="16" fill="rgba(255,255,255,.85)" stroke="#f9c22e" stroke-width="2"/><path d="M14 10 L26 18 L14 26Z" fill="#f9c22e"/></svg>
<p class="abs story">Our crew is reaching out to local clubs and the wider flying community to begin exploring what kind of shared booking system will be needed to support safe weekend trips for members. We caught up with the new trainer at the annual fly-in at Harrow Field, and while we weren't entirely</p>
<div class="abs btn-outline btn-more">More</div>

<footer class="abs footer"></footer>
<ul class="abs footer-nav">
  <li>Home</li><li>Aircraft</li><li>Airport</li><li>Pilots</li><li>Pilots</li><li>Passengers</li><li>Events</li><li>Contact</li>
</ul>
<div class="abs signup"><span>Sign up to Stay Informed</span><b>Send</b></div>
<div class="abs social social-foot" aria-label="Social links"><b></b><b></b><b></b><b></b><b></b></div>

</body>
</html>
```